Designer Instructions – Updated Referral Program Flyer

(Based on the mock-up in “Brief Layout and Instructions.pdf”)

OVERALL STYLE + LAYOUT

Maintain the same general layout, structure, and flow as the mock-up flyer (front and back).

This is an update of an older flyer, not a full redesign — keep the same sections, proportions, and overall visual feel, but with cleaner, more modern design improvements.

The final flyer should look clean, bold, professional, and high-impact, geared toward realtors, property managers, and contractors who refer work.

FRONT SIDE INSTRUCTIONS
1. Header Section

Remove the Tallow Ridge Builders logo from the top banner.
(Shown on page 1 of the PDF)

2. Main Headline

Keep the same three-line structure:
EARN
UNLIMITED
CASH

Center it, maximize impact, and increase the font size of CASH so all three words match in importance.

Make the headline bold, clean, and the main focal point.

3. Cash Incentive Box

Keep the "$500 minimum OR 10% per referral" box, but upgrade the graphics to look sharper and more modern.

Ensure the wording matches exactly what’s in the mock-up.

4. Premier Partner Program Ribbon

Clean up and modernize the "PREMIER PARTNER PROGRAM" bar while keeping the same position and structure.

Ensure the checkmark badge remains crisp and professional.

5. Supporting Icons Section

Keep the four icons/benefit boxes (Guaranteed Payout, Free Evaluations, Affordable Solutions, Industry Leaders) in the same order.

Update the icons to cleaner, more modern styles — but maintain the same meanings.

Improve alignment and spacing for sharper visual consistency.

6. Remove Icons in Contact Area

At the bottom (“CALL TEXT OR BOOK ONLINE 555-014-2796 TallowRidgeBuilders.example”), remove the phone and internet icons, as noted on page 2 of the PDF.

7. Replace All Images

I (Darnell) will provide all updated stock images separately via email.

Replace the flood/water-damage imagery and roof leak with the new images I send.

Keep image placement and proportions the same as the mock-up.

BACK SIDE INSTRUCTIONS
1. Header Image + “REFER / EARN” Section

Maintain the same large split-image layout (“The more you refer, the more you earn”).

Replace all background imagery with the new assets I will send.

Keep the CASH FLOW image section but modernize the type and spacing.

2. “HOW IT WORKS” Section

Preserve the three-column layout:

Refer Flood, Water & Mold Damage

We Take Care of Everything (evaluations/insurance)

Get Paid to Share

Update images, tighten spacing, and use modern iconography.

3. Remove Phone/Internet Icons

Same as the front side — remove small communication icons and keep only the text/number/URL.

4. Bottom Contact Bar

Keep the blue bar, same wording, same layout — just modernize the style if needed for clarity.

5. Replace All Back-Side Images

Again, I will email you the image assets.

Keep the layout EXACT — just update with higher-quality photos and improved design.

TEXT CONTENT (Keep as-is unless spacing adjustments needed)

All text shown in the PDF should remain exactly the same unless spacing or visual balance requires minor adjustments.
Example from page 3:

“REFER FLOOD, MOLD & CONSTRUCTION JOBS”

“We Schedule a Free Estimate. If Approved, You Get Paid.”

“Everybody Benefits From Referrals”

Everything stays, just refreshed and visually improved.

DESIGN GOALS

Flyer should look high-end and trustworthy, not salesy.

Consistent color theme: blues, whites, yellows, same palette as original.

Use bold, modern fonts with strong readability.

Ensure all headlines pop and all benefit boxes are clean, well-aligned, and evenly spaced.

The final result should feel like a premium referral program flyer for a top-tier restoration/remodel company.

FILES I WILL PROVIDE

I will send the designer:

All replacement stock photos

Any updated logos (if needed)

Original high-resolution version of the mock-up (if available)

Any additional icons preferred

0054AA
0677BA
7BADD7
CADEEF
E8F1F8

• Designer Instructions – Updated Referral Program Flyer (Based on the mock-up in “Brief Layout and Instructions.pdf”) OVERALL STYLE + LAYOUT Maintain the same general layout, structure, and flow as the mock-up flyer (front and back). This is an update of an older flyer, not a full redesign — keep the same sections, proportions, and overall visual feel, but with cleaner, more modern design improvements. The final flyer should look clean, bold, professional, and high-impact, geared toward realtors, property managers, and contractors who refer work. FRONT SIDE INSTRUCTIONS 1. Header Section Remove the Tallow Ridge Builders logo from the top banner. (Shown on page 1 of the PDF) 2. Main Headline Keep the same three-line structure: EARN UNLIMITED CASH Center it, maximize impact, and increase the font size of CASH so all three words match in importance. Make the headline bold, clean, and the main focal point. 3. Cash Incentive Box Keep the "$500 minimum OR 10% per referral" box, but upgrade the graphics to look sharper and more modern. Ensure the wording matches exactly what’s in the mock-up. 4. Premier Partner Program Ribbon Clean up and modernize the "PREMIER PARTNER PROGRAM" bar while keeping the same position and structure. Ensure the checkmark badge remains crisp and professional. 5. Supporting Icons Section Keep the four icons/benefit boxes (Guaranteed Payout, Free Evaluations, Affordable Solutions, Industry Leaders) in the same order. Update the icons to cleaner, more modern styles — but maintain the same meanings. Improve alignment and spacing for sharper visual consistency. 6. Remove Icons in Contact Area At the bottom (“CALL TEXT OR BOOK ONLINE 555-014-2796 TallowRidgeBuilders.example”), remove the phone and internet icons, as noted on page 2 of the PDF. 7. Replace All Images I (Darnell) will provide all updated stock images separately via email. Replace the flood/water-damage imagery and roof leak with the new images I send. Keep image placement and proportions the same as the mock-up. BACK SIDE INSTRUCTIONS 1. Header Image + “REFER / EARN” Section Maintain the same large split-image layout (“The more you refer, the more you earn”). Replace all background imagery with the new assets I will send. Keep the CASH FLOW image section but modernize the type and spacing. 2. “HOW IT WORKS” Section Preserve the three-column layout: Refer Flood, Water & Mold Damage We Take Care of Everything (evaluations/insurance) Get Paid to Share Update images, tighten spacing, and use modern iconography. 3. Remove Phone/Internet Icons Same as the front side — remove small communication icons and keep only the text/number/URL. 4. Bottom Contact Bar Keep the blue bar, same wording, same layout — just modernize the style if needed for clarity. 5. Replace All Back-Side Images Again, I will email you the image assets. Keep the layout EXACT — just update with higher-quality photos and improved design. TEXT CONTENT (Keep as-is unless spacing adjustments needed) All text shown in the PDF should remain exactly the same unless spacing or visual balance requires minor adjustments. Example from page 3: “REFER FLOOD, MOLD & CONSTRUCTION JOBS” “We Schedule a Free Estimate. If Approved, You Get Paid.” “Everybody Benefits From Referrals” Everything stays, just refreshed and visually improved. DESIGN GOALS Flyer should look high-end and trustworthy, not salesy. Consistent color theme: blues, whites, yellows, same palette as original. Use bold, modern fonts with strong readability. Ensure all headlines pop and all benefit boxes are clean, well-aligned, and evenly spaced. The final result should feel like a premium referral program flyer for a top-tier restoration/remodel company. FILES I WILL PROVIDE I will send the designer: All replacement stock photos Any updated logos (if needed) Original high-resolution version of the mock-up (if available) Any additional icons preferred

```html
<!DOCTYPE html>
<html lang="en">
<head>
<meta charset="utf-8">
<title>Premier Partner Referral Program Flyer</title>
<link href="https://fonts.googleapis.com/css2?family=Anton&family=Poppins:wght@400;500;600;700;800&display=swap" rel="stylesheet">
<style>
  :root{
    --stage:#a9a9a9;
    --blue:#2e3593;
    --blue-steel:#2f5a94;
    --navy:#13223b;
    --yellow:#eec43a;
    --red:#d63a3a;
    --white:#ffffff;
    --ink:#333333;
    --grey-line:#c9c9c9;
  }
  *{margin:0;padding:0;box-sizing:border-box}
  html,body{width:949px;height:1200px;overflow:hidden}
  body{background:var(--stage);font-family:'Poppins',sans-serif;position:relative}
  .flyer{position:absolute;left:93px;width:764px;height:494px;background:var(--white);overflow:hidden}
  .flyer--front{top:87px}
  .flyer--back{top:619px}
  .shapes{position:absolute;left:0;top:0}

  /* front header */
  .photo-skyline{position:absolute;left:0;top:0;width:764px;height:208px;
    clip-path:polygon(396px 0,764px 0,764px 208px,418px 208px,328px 88px);
    background:linear-gradient(180deg,#6d5a8f 0%,#b07a7a 35%,#c98a4a 55%,#4a3f6e 70%,#3b3f78 100%)}
  .headline{position:absolute;left:40px;width:310px;text-align:center;font-weight:800;line-height:1;letter-spacing:-.5px}
  .headline--earn{top:19px;font-size:50px;color:var(--yellow)}
  .headline--unlimited{top:71px;font-size:37px;color:var(--white);font-weight:700}
  .headline--cash{top:109px;font-size:49px;color:var(--yellow)}
  .ribbon-text{position:absolute;font-weight:700;color:var(--blue);line-height:1;text-align:center}
  .ribbon-text--front{left:90px;width:320px;top:180px;font-size:17px}

  /* incentive */
  .incentive-amount{position:absolute;color:var(--white);line-height:1;white-space:nowrap}
  .incentive-amount b{font-weight:800;display:block}
  .incentive-amount span{font-size:16px;font-weight:500;display:block}
  .incentive-amount--min{left:47px;top:232px}
  .incentive-amount--min b{font-size:25px}
  .incentive-amount--min span{margin-top:4px}
  .incentive-amount--pct{left:227px;top:251px}
  .incentive-amount--pct b{font-size:24px}
  .incentive-amount--pct span{margin-top:5px}
  .or-label{position:absolute;left:152px;top:254px;width:44px;text-align:center;font-weight:800;font-size:17px;line-height:1;color:#111}
  .premier-label{position:absolute;left:490px;width:150px;top:215px;text-align:center;font-size:19px;font-weight:500;color:var(--ink);line-height:1}
  .program-word{position:absolute;top:261px;font-size:24px;font-weight:800;color:var(--white);line-height:1}

  .wins{position:absolute;left:0;width:764px;top:318px;text-align:center;font-size:27px;font-weight:800;color:var(--blue);line-height:1}

  .benefits{position:absolute;left:24px;top:359px;display:flex;gap:3px}
  .benefit{position:relative;width:177px;height:56px;border-radius:28px;border:2px solid var(--blue);background:var(--white)}
  .benefit--gold{border-color:var(--yellow)}
  .benefit__icon{position:absolute;left:4px;top:6px;width:40px;height:40px}
  .benefit__title{position:absolute;left:54px;top:9px;font-size:8.4px;font-weight:700;color:#222;line-height:1;white-space:nowrap}
  .benefit__text{position:absolute;left:54px;top:25px;font-size:7.6px;line-height:12.5px;color:#444;white-space:nowrap}

  .slogan{position:absolute;left:0;width:764px;top:426px;text-align:center;font-size:19.5px;font-weight:700;line-height:1;color:var(--blue)}
  .slogan em{font-style:normal;color:var(--red)}

  .contact-call{position:absolute;left:44px;top:467px;font-size:16px;font-weight:700;color:var(--white);line-height:1}
  .contact-call span{font-weight:400}
  .contact-phone{position:absolute;left:395px;top:468px;font-size:13.5px;font-weight:700;color:var(--blue);line-height:1}
  .contact-web{position:absolute;left:505px;top:469px;font-size:12.5px;font-weight:700;color:var(--blue);line-height:1;white-space:nowrap}

  /* back header */
  .photo-cash{position:absolute;left:0;top:0;width:764px;height:208px;
    clip-path:polygon(396px 0,764px 0,764px 208px,418px 208px,326px 88px);
    background:linear-gradient(135deg,#e9e9e9 0%,#c7c9cc 40%,#8fd3d6 55%,#b9bbbf 70%,#e3e3e3 100%)}
  .ribbon-text--back{left:270px;width:220px;top:180px;font-size:19px}

  .step-photo{position:absolute;top:225px;width:232px;height:132px}
  .step-photo--equipment{left:22px;background:linear-gradient(135deg,#d9d6d0 0%,#4fa3c8 45%,#2b7fae 70%,#c9c4bb 100%)}
  .step-photo--house{left:266px;background:linear-gradient(160deg,#f1f1ee 0%,#cfd3d4 40%,#7fa15a 75%,#4f7a3a 100%)}
  .step-photo--sign{left:510px;background:linear-gradient(135deg,#5b8fd0 0%,#cfe0f3 40%,#f2e02a 60%,#5a8bcf 100%)}
  .step-card{position:absolute;top:357px;height:81px;border:1.5px solid var(--grey-line);border-top:none;background:var(--white)}
  .step-card h3{position:absolute;font-size:11.5px;font-weight:700;color:var(--blue);line-height:15.5px;top:10px;white-space:nowrap}
  .step-card p{position:absolute;font-size:9.8px;color:var(--ink);line-height:15px;top:44px;white-space:nowrap}
</style>
</head>
<body>

<section class="flyer flyer--front">
  <svg class="shapes" width="764" height="494" viewBox="0 0 764 494">
    <polygon points="0,0 396,0 328,88 418,208 0,208" fill="var(--blue)"/>
    <polygon points="70,172 395,172 420,208 70,208 82,190" fill="var(--yellow)"/>
    <polygon points="18,225 182,225 152,284 18,284" fill="var(--red)"/>
    <polygon points="168,243 374,243 374,303 150,303" fill="var(--blue)"/>
    <circle cx="174" cy="263" r="29" fill="var(--white)"/>
    <polygon points="390,243 558,243 548,303 390,303" fill="var(--red)"/>
    <polygon points="566,243 747,243 747,303 548,303" fill="var(--blue)"/>
    <circle cx="563" cy="272" r="24" fill="var(--white)"/>
    <circle cx="563" cy="270" r="10" fill="var(--red)"/>
    <circle cx="563" cy="270" r="6.5" fill="none" stroke="var(--white)" stroke-width="1.4"/>
    <polyline points="559.5,270 562,272.5 566.5,267.5" fill="none" stroke="var(--white)" stroke-width="1.5"/>
    <polygon points="556,278 559,288 563,283 567,288 570,278" fill="var(--red)"/>
    <rect x="0" y="458" width="764" height="36" fill="var(--yellow)"/>
    <polygon points="0,458 330,458 362,494 0,494" fill="var(--blue)"/>
  </svg>
  <div class="photo-skyline" role="img" aria-label="City skyline at dusk reflected on a bay"></div>

  <div class="headline headline--earn">EARN</div>
  <div class="headline headline--unlimited">UNLIMITED</div>
  <div class="headline headline--cash">CASH</div>
  <div class="ribbon-text ribbon-text--front">GET PAID TO REFER A FLOOD</div>

  <div class="incentive-amount incentive-amount--min"><b>$500</b><span>MINIMUM</span></div>
  <div class="or-label">OR</div>
  <div class="incentive-amount incentive-amount--pct"><b>10%</b><span>PER REFERRAL!</span></div>

  <div class="premier-label">PREMIER</div>
  <div class="program-word" style="left:408px">PARTNER</div>
  <div class="program-word" style="left:599px">PROGRAM</div>

  <div class="wins">PARTNER WITH US &amp; EVERYBODY WINS!</div>

  <div class="benefits">
    <div class="benefit">
      <svg class="benefit__icon" viewBox="0 0 40 40"><circle cx="20" cy="20" r="20" fill="var(--blue)"/><circle cx="21" cy="19" r="8" fill="none" stroke="#fff" stroke-width="1.6"/><text x="21" y="23" text-anchor="middle" font-family="Poppins,sans-serif" font-size="11" font-weight="700" fill="#fff">$</text></svg>
      <div class="benefit__title">GUARANTEED PAYOUT*</div>
      <div class="benefit__text">Minimum $500 or 10% of<br>Total Invoice Paid Fast</div>
    </div>
    <div class="benefit benefit--gold">
      <svg class="benefit__icon" viewBox="0 0 40 40"><circle cx="20" cy="20" r="20" fill="var(--yellow)"/><rect x="12" y="11" width="13" height="17" rx="1.5" fill="none" stroke="var(--blue)" stroke-width="1.6"/><text x="18.5" y="23" text-anchor="middle" font-family="Poppins,sans-serif" font-size="9" font-weight="700" fill="var(--blue)">%</text><circle cx="27" cy="26" r="5" fill="var(--yellow)" stroke="var(--blue)" stroke-width="1.4"/></svg>
      <div class="benefit__title">FREE ESTIMATES</div>
      <div class="benefit__text">Fast &amp; Free Inspections &amp;<br>Written Estimates</div>
    </div>
    <div class="benefit">
      <svg class="benefit__icon" viewBox="0 0 40 40"><circle cx="20" cy="20" r="20" fill="var(--blue)"/><circle cx="20" cy="20" r="9" fill="none" stroke="#fff" stroke-width="1.6"/><polyline points="15.5,20 19,23.5 25,16.5" fill="none" stroke="#fff" stroke-width="1.8"/></svg>
      <div class="benefit__title">AFFORDABLE SOLUTIONS</div>
      <div class="benefit__text">Lowest Out of Pocket<br>Costs for Your Customers</div>
    </div>
    <div class="benefit benefit--gold">
      <svg class="benefit__icon" viewBox="0 0 40 40"><circle cx="20" cy="20" r="20" fill="var(--yellow)"/><circle cx="20" cy="13" r="3" fill="none" stroke="var(--blue)" stroke-width="1.4"/><circle cx="13" cy="22" r="2.6" fill="none" stroke="var(--blue)" stroke-width="1.4"/><circle cx="27" cy="22" r="2.6" fill="none" stroke="var(--blue)" stroke-width="1.4"/><path d="M9 30 q4-5 8 0 M16 30 q4-6 8 0 M23 30 q4-5 8 0" fill="none" stroke="var(--blue)" stroke-width="1.4"/></svg>
      <div class="benefit__title">INDUSTRY LEADERS</div>
      <div class="benefit__text">Licensed &amp; Certified Experts<br>Provide 100% Guarantee</div>
    </div>
  </div>

  <div class="slogan">SEND <em>REFERRALS.</em>GET <em>PAID.</em>GROW <em>YOUR BUSINESS</em></div>

  <div class="contact-call">CALL, TEXT <span>OR</span> BOOK ONLINE</div>
  <div class="contact-phone">555-014-2796</div>
  <div class="contact-web">www.TallowRidgeBuilders.example</div>
</section>

<section class="flyer flyer--back">
  <svg class="shapes" width="764" height="494" viewBox="0 0 764 494">
    <defs>
      <linearGradient id="goldText" x1="0" y1="0" x2="1" y2="1">
        <stop offset="0" stop-color="#f7e21a"/><stop offset="1" stop-color="#efa91c"/>
      </linearGradient>
      <clipPath id="headerClip"><rect x="0" y="0" width="764" height="208"/></clipPath>
    </defs>
    <polygon points="0,0 396,0 326,88 418,208 0,208" fill="var(--blue-steel)"/>
    <polygon points="50,208 50,16 200,16 275,70 275,208" fill="var(--navy)"/>
    <g clip-path="url(#headerClip)" font-family="Anton,sans-serif">
      <text x="50" y="42" textLength="150" lengthAdjust="spacingAndGlyphs" font-size="28" fill="#fff">THE MORE YOU</text>
      <text x="50" y="105" textLength="150" lengthAdjust="spacingAndGlyphs" font-size="64" fill="url(#goldText)">REFER</text>
      <text x="50" y="135" textLength="150" lengthAdjust="spacingAndGlyphs" font-size="28" fill="#fff">THE MORE YOU</text>
      <text x="50" y="216" textLength="150" lengthAdjust="spacingAndGlyphs" font-size="84" fill="url(#goldText)">EARN</text>
    </g>
    <rect x="0" y="458" width="764" height="36" fill="var(--yellow)"/>
    <polygon points="0,458 330,458 362,494 0,494" fill="var(--blue)"/>
  </svg>
  <div class="photo-cash" role="img" aria-label="Scattered banknotes with tiled letter blocks spelling cash flow"></div>
  <svg class="shapes" width="764" height="494" viewBox="0 0 764 494">
    <polygon points="262,172 470,172 498,208 262,208 274,190" fill="var(--yellow)"/>
  </svg>
  <div class="ribbon-text ribbon-text--back">HOW IT WORKS</div>

  <div class="step-photo step-photo--equipment" role="img" aria-label="Drying fans and dehumidifiers in a water-damaged room"></div>
  <div class="step-photo step-photo--house" role="img" aria-label="Inspector holding a work estimate in front of a house"></div>
  <div class="step-photo step-photo--sign" role="img" aria-label="Yellow road sign reading get paid to share against a blue sky"></div>

  <div class="step-card" style="left:34px;width:207px">
    <h3 style="left:30px">REFER FLOOD, MOLD &amp;<br>CONSTRUCTION JOBS:</h3>
    <p style="left:30px">It’s Simple to Refer 24/7:<br>Call, Text or Book Online.</p>
  </div>
  <div class="step-card" style="left:282px;width:200px">
    <h3 style="left:30px">WE TAKE CARE OF<br>EVERYTHING:</h3>
    <p style="left:30px">We Schedule a Free Estimate.<br>If Approved, You Get Paid.</p>
  </div>
  <div class="step-card" style="left:530px;width:193px">
    <h3 style="left:31px">EVERYBODY BENEFITS<br>FROM REFERRALS</h3>
    <p style="left:31px">It’s Simple to Refer 24/7:<br>Call, Text or Book Online.</p>
  </div>

  <div class="contact-call">CALL, TEXT <span>OR</span> BOOK ONLINE</div>
  <div class="contact-phone">555-014-2796</div>
  <div class="contact-web">www.TallowRidgeBuilders.example</div>
</section>

</body>
</html>
```